Tidewell Homecare

I am looking to have a website designed for a housekeeping company that looks similar to this one. https://marlowsnestcare.example/

I need 5 websites designed but will start with this one to see how I like it.

Industry/Entity Type

House Cleaning

Coding

Coded - Design and coding required

Number of Pages Required

5+ page

Font styles to use
Serif
Script

Colors
ffffff
fdf9cf
fbf289
fbee3f
d6edf3
86cae7
33a6d7
edf1f8
cedeed

```html
<!DOCTYPE html>
<html lang="en">
<head>
<meta charset="utf-8">
<title>Tidewell Homecare</title>
<link href="https://fonts.googleapis.com/css2?family=Fira+Sans:wght@400;500;600;700&family=Great+Vibes&display=swap" rel="stylesheet">
<style>
:root{
  --teal:#6cc4c8;
  --teal-dark:#5bb6ba;
  --white:#ffffff;
  --ink:#3a3a3a;
  --nav:#6f6f6f;
  --accent:#f08a7e;
  --label:#7a7a7a;
  --mint:#a6e3c6;
  --salmon:#f4918a;
  --lime:#d6d95a;
  --leaf:#a4c96a;
  --curve:#9cc765;
}
*{box-sizing:border-box;margin:0;padding:0}
html,body{width:1200px;height:964px;overflow:hidden;background:var(--white);font-family:"Fira Sans",sans-serif}
.page{position:relative;width:1200px;height:964px}
.topbar{position:absolute;left:0;top:0;width:1200px;height:42px;background:var(--teal)}
.topbar .info{position:absolute;top:0;height:42px;display:flex;align-items:center;gap:8px;color:var(--white);font-weight:600;font-size:12.5px}
.topbar .phone{left:237px}
.topbar .hours{left:369px}
.social{position:absolute;left:678px;top:12px;display:flex;gap:8px}
.social span{width:20px;height:20px;border-radius:50%;background:var(--white)}
.social span.alt{background:#4fd0e0;border:1px solid #8fe0ea}
.btn{position:absolute;top:9px;height:26px;border-radius:3px;background:var(--white);color:var(--teal);font-size:8px;font-weight:600;letter-spacing:.4px;display:flex;align-items:center;justify-content:center}
.btn.quote{left:801px;width:74px}
.btn.calc{left:887px;width:73px}
.brand{position:absolute;left:0;top:70px;width:1200px;height:72px;display:flex;justify-content:center;align-items:center}
.brand .name{font-family:"Great Vibes",cursive;font-size:50px;font-weight:400;color:var(--ink);line-height:1}
.nav{position:absolute;top:168px;left:0;width:1200px;height:18px}
.nav a{position:absolute;transform:translateX(-50%);font-size:9.5px;font-weight:600;color:var(--nav);text-decoration:none;letter-spacing:.2px}
.nav a.active{color:var(--accent)}
.nav .search{position:absolute;left:950px;top:0}
.hero{position:absolute;left:0;top:200px;width:1200px;height:540px}
.services{position:absolute;left:0;top:798px;width:1200px}
.service{position:absolute;width:150px;transform:translateX(-50%);text-align:center}
.service svg{display:block;margin:0 auto}
.service p{margin-top:14px;font-size:10.5px;font-weight:500;color:var(--label)}
</style>
</head>
<body>
<div class="page">
  <header class="topbar">
    <div class="info phone">
      <svg width="20" height="18" viewBox="0 0 20 18"><path d="M2 6c0-3 4-4 8-4s8 1 8 4v1h-4V5H6v2H2z" fill="#fff"/><path d="M5 8h10l2 8H3z" fill="#fff"/><circle cx="10" cy="12" r="2.4" fill="#6cc4c8"/></svg>
      <span>(555) 014-2270</span>
    </div>
    <div class="info hours">
      <svg width="20" height="20" viewBox="0 0 20 20"><circle cx="10" cy="10" r="8.5" fill="none" stroke="#fff" stroke-width="1.6"/><path d="M10 5v5h4" fill="none" stroke="#fff" stroke-width="1.6"/></svg>
      <span>24 hours</span>
    </div>
    <div class="social"><span></span><span></span><span class="alt"></span><span class="alt"></span></div>
    <a class="btn quote">GET A QUOTE</a>
    <a class="btn calc">CALCULATOR</a>
  </header>

  <div class="brand"><span class="name">Tidewell Homecare</span></div>

  <nav class="nav">
    <a class="active" style="left:386px">HOME</a>
    <a style="left:461px">ABOUT</a>
    <a style="left:537px">PAGES</a>
    <a style="left:619px">SERVICES</a>
    <a style="left:697px">BLOG</a>
    <a style="left:780px">CONTACTS</a>
    <svg class="search" width="12" height="12" viewBox="0 0 12 12"><circle cx="5" cy="5" r="3.8" fill="none" stroke="#333" stroke-width="1.8"/><path d="M7.8 7.8L11 11" stroke="#333" stroke-width="2"/></svg>
  </nav>

  <svg class="hero" width="1200" height="540" viewBox="0 0 1200 540" role="img" aria-label="Photo of a bright white kitchen with a teal island, pendant lights and bar stools">
    <defs>
      <linearGradient id="heroFill" x1="0" y1="0" x2="0" y2="1">
        <stop offset="0" stop-color="#eee6d6"/>
        <stop offset=".22" stop-color="#f5f1e8"/>
        <stop offset=".5" stop-color="#eef0ee"/>
        <stop offset=".66" stop-color="#b9c9c6"/>
        <stop offset=".76" stop-color="#4fa8ae"/>
        <stop offset=".88" stop-color="#3e8d94"/>
        <stop offset="1" stop-color="#3a474c"/>
      </linearGradient>
      <linearGradient id="heroSide" x1="0" y1="0" x2="1" y2="0">
        <stop offset="0" stop-color="#8fb2b6" stop-opacity=".6"/>
        <stop offset=".25" stop-color="#ffffff" stop-opacity="0"/>
        <stop offset=".75" stop-color="#ffffff" stop-opacity="0"/>
        <stop offset=".88" stop-color="#9fc1c4" stop-opacity=".45"/>
        <stop offset="1" stop-color="#f4f6ef" stop-opacity=".7"/>
      </linearGradient>
    </defs>
    <path d="M0 0H1200V488Q600 580 0 488Z" fill="url(#heroFill)"/>
    <path d="M0 0H1200V488Q600 580 0 488Z" fill="url(#heroSide)"/>
    <path d="M0 488Q600 580 1200 488V500Q600 545 0 500Z" fill="#ffffff"/>
    <path d="M0 488Q600 580 1200 488" fill="none" stroke="var(--curve)" stroke-width="3.5"/>
  </svg>

  <section class="services">
    <div class="service" style="left:297px">
      <svg width="108" height="108" viewBox="0 0 108 108"><circle cx="54" cy="54" r="52" fill="none" stroke="var(--mint)" stroke-width="2"/><circle cx="54" cy="54" r="45" fill="var(--mint)"/>
        <path d="M48 36h12v6l4 4v24H44V46l4-4z" fill="#fff"/><rect x="52" y="30" width="8" height="5" fill="#fff"/><rect x="44" y="72" width="20" height="4" rx="2" fill="#fff"/></svg>
      <p>Maid Services</p>
    </div>
    <div class="service" style="left:449px">
      <svg width="108" height="108" viewBox="0 0 108 108"><circle cx="54" cy="54" r="52" fill="none" stroke="var(--teal-dark)" stroke-width="2"/><circle cx="54" cy="54" r="45" fill="var(--teal)"/>
        <path d="M36 32h28l-2 18H48z" fill="#fff"/><path d="M50 52l9 22" stroke="#fff" stroke-width="6" stroke-linecap="round"/></svg>
      <p>Window Cleaning</p>
    </div>
    <div class="service" style="left:600px">
      <svg width="108" height="108" viewBox="0 0 108 108"><circle cx="54" cy="54" r="52" fill="none" stroke="var(--salmon)" stroke-width="2"/><circle cx="54" cy="54" r="45" fill="var(--salmon)"/>
        <path d="M42 48h26l-3 26H45z" fill="#fff"/><path d="M62 46l8-12" stroke="#fff" stroke-width="4" stroke-linecap="round"/><ellipse cx="36" cy="72" rx="4" ry="2" fill="#fff"/></svg>
      <p>Domestic Cleaning</p>
    </div>
    <div class="service" style="left:751px">
      <svg width="108" height="108" viewBox="0 0 108 108"><circle cx="54" cy="54" r="52" fill="none" stroke="var(--lime)" stroke-width="2"/><circle cx="54" cy="54" r="45" fill="var(--lime)"/>
        <path d="M40 72V42a8 8 0 0 1 16 0v10" fill="none" stroke="#fff" stroke-width="5"/><rect x="50" y="52" width="20" height="20" rx="6" fill="#fff"/><rect x="34" y="70" width="14" height="4" fill="#fff"/><circle cx="58" cy="70" r="4" fill="var(--lime)" stroke="#fff" stroke-width="2"/></svg>
      <p>Office Cleaning</p>
    </div>
    <div class="service" style="left:902px">
      <svg width="108" height="108" viewBox="0 0 108 108"><circle cx="54" cy="54" r="52" fill="none" stroke="var(--leaf)" stroke-width="2"/><circle cx="54" cy="54" r="45" fill="var(--leaf)"/>
        <path d="M36 60l14-10 16 16-14 8z" fill="#fff"/><path d="M58 52l12-20" stroke="#fff" stroke-width="5" stroke-linecap="round"/><path d="M38 44l2-4 2 4-2 4z" fill="#fff"/></svg>
      <p>Carpet Steam Cleaning</p>
    </div>
  </section>
</div>
</body>
</html>
```